Label Design Project for my tea product Imported from Japan

I have a tea importing business. I want someone to help me design a label for my Uji matcha tea product. I want the label to be modern, neat, and beautifully designed. I prefer it to be easily adaptable to other tea products that I will be importing.
Product name: Organic Hoshiba Matcha
Company name: Calm Harbor Leaf Merchants
Description: Powdered Green Tea Matcha
Ceremonial grade premium quality
Directly imported from Japan
This product is going to be sold in the U.S. market, so please make sure that the label is in compliance with the BQC regulations.

Target Market(s)

High end tea consumers

Industry/Entity Type

Business

Requirements
Must have
• Marking of origin : product of Japan
• Imported by: Calm Harbor Leaf Merchants
• Leave space for Net weight, the name and place of business of the manufacturer.
• Ingredients: Green Tea 100%
• Nutrition list is not necessary.

```html
<!DOCTYPE html>
<html lang="en">
<head>
<meta charset="utf-8">
<title>Organic Hoshiba Matcha Label</title>
<link rel="stylesheet" href="https://fonts.googleapis.com/css2?family=Arimo:wght@400;700&family=Permanent+Marker&display=swap">
<style>
  :root {
    --page: #ffffff;
    --band: #2f6b22;
    --cream: #fbf6d2;
    --cream-deep: #f3ecc0;
    --leaf: #7fb64a;
    --ink: #111111;
    --band-ink: #10240b;
  }
  * { box-sizing: border-box; margin: 0; padding: 0; }
  html, body {
    width: 720px; height: 1200px; overflow: hidden;
    background: var(--page);
  }
  .label {
    position: absolute; left: 38px; top: 38px;
    width: 640px; height: 1117px;
    background: var(--cream);
    overflow: hidden;
  }
  .band-top {
    position: absolute; left: 0; top: 0; width: 100%; height: 68px;
    background: var(--band);
  }
  .leaf-pattern {
    position: absolute; left: 0; top: 68px; width: 100%; height: 928px;
    background:
      repeating-linear-gradient(90deg, transparent 0 72px, rgba(127,182,74,0.18) 72px 78px, transparent 78px 160px),
      linear-gradient(180deg, var(--cream), var(--cream-deep));
  }
  .title-block {
    position: absolute; left: 0; top: 250px; width: 100%;
    text-align: center; color: var(--ink);
  }
  .title-organic {
    font-family: "Arimo", Arial, sans-serif;
    font-weight: 700; font-size: 40px; letter-spacing: 2px;
    line-height: 1;
  }
  .title-name {
    font-family: "Permanent Marker", cursive;
    font-weight: 400; line-height: 1;
    letter-spacing: 4px;
  }
  .title-name.first { font-size: 104px; margin-top: 20px; }
  .title-name.second { font-size: 104px; margin-top: 8px; }
  .title-desc {
    font-family: "Arimo", Arial, sans-serif;
    font-weight: 700; font-size: 25px; letter-spacing: 0.5px;
    margin-top: 46px;
  }
  .band-bottom {
    position: absolute; left: 0; bottom: 0; width: 100%; height: 121px;
    background: var(--band);
    font-family: "Arimo", Arial, sans-serif;
    color: var(--band-ink);
  }
  .origin {
    position: absolute; left: 32px; top: 36px;
    font-size: 21px; line-height: 1.3;
  }
  .importer {
    position: absolute; left: 232px; top: 62px;
    font-size: 21px;
  }
  .importer-name {
    position: absolute; left: 444px; top: 48px; width: 180px;
    display: flex; align-items: center; gap: 8px;
    font-size: 15px; line-height: 1.15; color: var(--leaf);
  }
  .importer-mark {
    flex: 0 0 14px; width: 14px; height: 14px; border-radius: 50%;
    background: var(--leaf);
  }
</style>
</head>
<body>
  <main class="label">
    <div class="band-top"></div>
    <div class="leaf-pattern" role="img" aria-label="Repeating pattern of green tea leaves on climbing vines over a cream background"></div>

    <header class="title-block">
      <p class="title-organic">ORGANIC</p>
      <h1 class="title-name first">HOSHIBA</h1>
      <p class="title-name second">MATCHA</p>
      <p class="title-desc">Powdered Organic Green Tea</p>
    </header>

    <footer class="band-bottom">
      <p class="origin">Product of Japan<br>Green Tea 100%</p>
      <p class="importer">Imported by</p>
      <p class="importer-name"><span class="importer-mark"></span>Calm Harbor Leaf Merchants</p>
    </footer>
  </main>
</body>
</html>
```